Sleep Consulting Business

Hello I need a business card design with similar colors to my logo that was created. I help mom/parents whose little ones are having sleep issues. Are you able to recreate the picture with the girl sleeping onto a business card using a picture that I provide. That would be one side with my logo on top and on the other side would the following:
My name (in bigger letters than the rest. maybe written in script
title
email
website
phone
instagram
I have included color Inspo
Full Name, number, email, website, ig page

```html
<!DOCTYPE html>
<html lang="en">
<head>
<meta charset="utf-8">
<title>Drift Away Sleep Co — Business Card</title>
<link rel="stylesheet" href="https://fonts.googleapis.com/css2?family=Josefin+Sans:wght@400;600&family=Alex+Brush&display=swap">
<style>
  :root {
    --rose: #bd8a76;
    --taupe: #8c7f7a;
    --ink: #5b5350;
    --card: #ffffff;
    --backdrop: #dcd9d6;
  }
  * { box-sizing: border-box; margin: 0; padding: 0; }
  html, body { width: 1200px; height: 900px; overflow: hidden; }
  body {
    background: var(--backdrop);
    display: flex;
    align-items: center;
    justify-content: center;
    gap: 70px;
    font-family: "Josefin Sans", sans-serif;
    color: var(--ink);
  }
  .card {
    position: relative;
    width: 380px;
    height: 665px;
    background: var(--card);
    box-shadow: 0 10px 30px rgba(0,0,0,.18);
    overflow: hidden;
  }
  .card-band { position: absolute; inset: 0; width: 100%; height: 100%; }
  .band-rose { fill: var(--rose); }
  .band-taupe { fill: var(--taupe); }
  .brand {
    position: absolute;
    text-align: center;
    width: 240px;
  }
  .brand-mark {
    display: block;
    width: 46px; height: 46px;
    margin: 0 auto 14px;
    border-radius: 50%;
    background: var(--taupe);
  }
  .brand-name {
    display: block;
    font-weight: 600;
    font-size: 30px;
    line-height: 1.15;
    letter-spacing: 2px;
    color: var(--taupe);
  }
  .front .brand { top: 70px; left: 115px; }
  .back .brand { top: 360px; left: 110px; }

  .person { position: absolute; left: 165px; top: 400px; }
  .person-name {
    font-family: "Alex Brush", cursive;
    font-size: 40px;
    color: var(--rose);
    line-height: 1;
  }
  .person-title { font-size: 19px; color: var(--ink); margin-top: 2px; }

  .contacts { position: absolute; left: 185px; top: 490px; list-style: none; }
  .contacts li {
    display: flex;
    align-items: flex-start;
    gap: 8px;
    font-size: 15px;
    line-height: 1.2;
    margin-bottom: 9px;
    color: var(--ink);
  }
  .contacts svg { flex: none; width: 15px; height: 15px; margin-top: 1px; }
  .icon-fill { fill: var(--rose); }
  .icon-line { fill: none; stroke: var(--rose); }
  .icon-cut { fill: none; stroke: #fff; stroke-width: 1.2; }
  .icon-hole { fill: #fff; }

  .site-vertical {
    position: absolute;
    left: 40px; top: 40px;
    writing-mode: vertical-rl;
    font-size: 17px;
    letter-spacing: 11px;
    color: var(--ink);
  }
  .site-vertical .accent { color: var(--rose); font-weight: 600; }
  .social-dot {
    position: absolute;
    left: 40px; bottom: 40px;
    width: 26px; height: 26px;
    border-radius: 50%;
    background: var(--rose);
  }
</style>
</head>
<body>

  <section class="card front" aria-label="Card front">
    <svg class="card-band" viewBox="0 0 380 665" preserveAspectRatio="none" aria-hidden="true">
      <path class="band-taupe" d="M0,104 C110,118 146,200 131,320 C116,440 116,570 208,665 L0,665 Z"/>
      <path class="band-rose" d="M0,100 C104,115 140,200 125,320 C110,440 110,570 198,665 L0,665 Z"/>
    </svg>
    <div class="brand">
      <span class="brand-mark"></span>
      <span class="brand-name">DRIFT AWAY<br>SLEEP CO</span>
    </div>
    <div class="person">
      <div class="person-name">Maren Holt</div>
      <div class="person-title">Director</div>
    </div>
    <ul class="contacts">
      <li>
        <svg viewBox="0 0 16 16"><path class="icon-fill" d="M4 1 L6.5 4 L5 6 C6 8.5 7.5 10 10 11 L12 9.5 L15 12 L13 15 C7 14 2 9 1 3 Z"/></svg>
        +91-120-5550172
      </li>
      <li>
        <svg viewBox="0 0 16 16"><rect class="icon-fill" x="1" y="3" width="14" height="10" rx="1"/><path class="icon-cut" d="M1.5 3.5 L8 9 L14.5 3.5"/></svg>
        hello@driftaway.in
      </li>
      <li>
        <svg viewBox="0 0 16 16"><circle class="icon-line" cx="8" cy="8" r="6.5" stroke-width="1.6"/><path class="icon-line" stroke-width="1.1" d="M1.5 8 H14.5 M8 1.5 C4.5 5 4.5 11 8 14.5 M8 1.5 C11.5 5 11.5 11 8 14.5"/></svg>
        www.driftaway.in
      </li>
      <li>
        <svg viewBox="0 0 16 16"><path class="icon-fill" d="M8 15 C4 10 3 8 3 6 A5 5 0 0 1 13 6 C13 8 12 10 8 15 Z"/><circle class="icon-hole" cx="8" cy="6" r="1.8"/></svg>
        <span>C-17 Lakeview Road,<br>Riverton 401220</span>
      </li>
    </ul>
  </section>

  <section class="card back" aria-label="Card back">
    <svg class="card-band" viewBox="0 0 380 665" preserveAspectRatio="none" aria-hidden="true">
      <path class="band-taupe" d="M292,0 C232,60 258,200 314,300 C362,385 376,470 380,600 L380,0 Z"/>
      <path class="band-rose" d="M300,0 C242,60 268,200 322,300 C366,382 380,460 380,560 L380,0 Z"/>
    </svg>
    <div class="site-vertical">www.<span class="accent">driftaway</span>.in</div>
    <div class="brand">
      <span class="brand-mark"></span>
      <span class="brand-name">DRIFT AWAY<br>SLEEP CO</span>
    </div>
    <span class="social-dot" aria-label="Social profile"></span>
  </section>

</body>
</html>
```